We need a business card and letterhead design for an orthodontic office. Needs to be clean, simple and sleek

Target Market(s)

adults/children

Industry/Entity Type

Dental

Contact Information for Business Card

Logo that is attached

Font styles to use
Serif

Colors

Designer to choose colors to be used in the design.

Requirements
Must have
• Martin L Okrand DDS
• Corinne Vesta DMD
• 82 Tolliver Avenue
• Dunwick,NY 11874
• (516) 472-9054
• www.okrandortho.example
Nice to have
• on the back.... space for appointment times
Should not have
• teeth

```html
<!DOCTYPE html>
<html lang="en">
<head>
<meta charset="utf-8">
<title>Okrand Orthodontics – Business Card</title>
<link rel="stylesheet" href="https://fonts.googleapis.com/css2?family=Jost:wght@300;400;500;600&display=swap">
<style>
  :root {
    --backdrop: #3b3431;
    --brand-blue: #5ea0cc;
    --brand-blue-deep: #3f8cc2;
    --card-white: #fbfbfb;
    --ink: #2a2a2a;
    --rule: #c9c9c9;
  }
  * { box-sizing: border-box; margin: 0; padding: 0; }
  html, body {
    width: 1200px; height: 715px; overflow: hidden;
    background: var(--backdrop);
    font-family: "Jost", sans-serif;
  }
  .canvas {
    position: relative; width: 1200px; height: 715px;
    display: flex; align-items: center; justify-content: center; gap: 40px;
  }
  .card {
    position: relative; width: 540px; height: 309px;
    border-radius: 3px; overflow: hidden;
    box-shadow: 0 12px 30px rgba(0,0,0,.45);
  }

  /* Back: appointment card */
  .card--back { background: var(--brand-blue); color: #fff; padding: 30px 36px; }
  .label {
    display: inline-block; background: #fff; color: var(--brand-blue);
    text-transform: uppercase; font-weight: 400; letter-spacing: .5px;
  }
  .label--title { font-size: 19px; padding: 5px 14px; margin-left: 160px; }
  .field { font-size: 13px; font-weight: 300; display: flex; align-items: flex-end; }
  .field .dots { flex: 1; border-bottom: 1.5px dotted rgba(255,255,255,.85); margin-left: 4px; height: 12px; }
  .row { display: flex; gap: 28px; margin-top: 14px; }
  .row .field { flex: 1; }
  .label--policy { font-size: 11px; padding: 2px 8px; margin: 26px 0 0 104px; }
  .policy { font-size: 13px; font-weight: 300; line-height: 1.45; margin-top: 6px; }

  /* Front: contact card */
  .card--front { background: var(--card-white); }
  .brand {
    position: absolute; left: 40px; top: 70px; width: 210px;
    color: var(--ink); font-weight: 300; text-transform: uppercase;
    font-size: 40px; line-height: 1; letter-spacing: 3px;
  }
  .brand small { display: block; font-size: 40px; }
  .brand .brand-sub { font-size: 40px; }
  .divider {
    position: absolute; left: 278px; top: 30px; width: 1.5px; height: 200px;
    background: linear-gradient(to bottom, transparent, var(--rule) 25%, #a9a9a9 60%, transparent);
  }
  .contact { position: absolute; left: 300px; top: 52px; color: var(--brand-blue-deep); }
  .person { font-size: 17px; font-weight: 600; line-height: 1.35; }
  .person .degree { color: var(--ink); font-size: 12px; font-weight: 400; margin-left: 6px; }
  .address { font-size: 14px; font-weight: 600; line-height: 1.3; margin-top: 14px; }
  .line { display: flex; align-items: center; gap: 10px; margin-top: 12px; color: var(--ink); font-size: 14px; }
  .line + .line { margin-top: 6px; }
  .line svg { flex: none; }
  .band {
    position: absolute; left: 0; right: 0; bottom: 0; height: 48px;
    background: var(--brand-blue); color: #fff;
    display: flex; align-items: center; justify-content: center;
    font-size: 15px; letter-spacing: 7px; font-weight: 500;
  }
</style>
</head>
<body>
<main class="canvas">

  <section class="card card--back" aria-label="Appointment card, back">
    <span class="label label--title">Next Appointment</span>
    <div class="row" style="margin-top:18px">
      <div class="field">Date:<span class="dots"></span></div>
      <div class="field" style="flex:.9">Time:<span class="dots"></span></div>
    </div>
    <div class="row">
      <div class="field">Appointment For:<span class="dots"></span></div>
    </div>
    <span class="label label--policy">Cancellation Policy</span>
    <p class="policy">If you are unable to keep your appointment, pl provide atleast<br>2 business daysnotice or full visit fee will apply.</p>
  </section>

  <section class="card card--front" aria-label="Business card, front">
    <div class="brand">Martin<br>Okrand<br><span style="font-size:19px;letter-spacing:2px;">Orthodontics</span></div>
    <div class="divider"></div>
    <div class="contact">
      <p class="person">Martin L Okrand<span class="degree">DDS</span></p>
      <p class="person">Corinne Vesta<span class="degree">DMD</span></p>
      <p class="address">82 Tolliver Avenue<br>Dunwick, NY 11874</p>
      <p class="line">
        <svg width="20" height="20" viewBox="0 0 20 20" aria-hidden="true"><circle cx="10" cy="10" r="10" fill="var(--brand-blue)"/><path d="M6 7.5c0-1 1-1.6 4-1.6s4 .6 4 1.6v1h-2v-.8H8v.8H6z M7 9.5h6l1 4H6z" fill="#fff"/></svg>
        (516) 472-9054
      </p>
      <p class="line">
        <svg width="20" height="20" viewBox="0 0 20 20" aria-hidden="true"><circle cx="10" cy="10" r="10" fill="var(--brand-blue)"/><rect x="5" y="6.5" width="10" height="7" fill="#fff"/><path d="M5 6.5l5 4 5-4" fill="none" stroke="var(--brand-blue)" stroke-width="1"/></svg>
        hello@okrandortho.example
      </p>
    </div>
    <div class="band">www.okrandortho.example</div>
  </section>

</main>
</body>
</html>
```